Interior Decoration and Concept Store needs a webpage design

Sophisticated website for my business, name Wren Hollow. Wren Hollow is a design service and homewares store run by interior decorator Marion Tulk.

Marion's qualification and work experience as an interior decorator, is able to provide advice and recommendations for interior and exterior concepts, colour consultations, furniture, lighting, decor concepts and products are sourced for individual projects. A re-upholstery service is also provided.

Facebook icon.
Projects page.
Profile page.
Established 2009
Medial page

Industry/Entity Type

Store

```html
<!DOCTYPE html>
<html lang="en">
<head>
<meta charset="utf-8">
<title>Wren Hollow – Interior Decoration</title>
<link rel="stylesheet" href="https://fonts.googleapis.com/css2?family=Open+Sans:ital,wght@0,300;0,400;0,600;1,400&display=swap">
<style>
  :root {
    --ink: #1f1f1f;
    --muted: #555555;
    --accent-red: #ef4b4f;
    --accent-green: #3cb44a;
    --accent-teal: #2a9a93;
    --rule: #cfcfcf;
    --footer-bg: #2a2927;
    --footer-text: #e6e6e6;
    --white: #ffffff;
    --swatch: #c25a5a;
  }
  * { margin: 0; padding: 0; box-sizing: border-box; }
  html, body { width: 1200px; height: 2880px; overflow: hidden; }
  body {
    position: relative;
    background: var(--white);
    font-family: "Open Sans", Arial, sans-serif;
    color: var(--ink);
  }
  .abs { position: absolute; }

  /* Header */
  .brand {
    left: 146px; top: 40px;
    font-size: 58px; font-weight: 400; letter-spacing: 1px;
    color: var(--ink); line-height: 1;
    display: flex; align-items: center; gap: 16px;
  }
  .brand-dot { width: 22px; height: 22px; border-radius: 50%; background: var(--ink); }
  .main-nav { left: 612px; top: 72px; width: 439px; height: 62px; }
  .main-nav ul { list-style: none; display: flex; }
  .main-nav li { position: absolute; font-size: 19px; top: 0; text-transform: uppercase; }
  .main-nav li.home { left: 8px; }
  .main-nav li.projects { left: 112px; }
  .main-nav li.profile { left: 240px; }
  .main-nav li.contact { left: 360px; }
  .nav-rule { left: 612px; top: 130px; width: 439px; height: 2px; background: var(--rule); }
  .nav-active { left: 612px; top: 124px; width: 68px; height: 7px; background: var(--accent-red); border-radius: 2px; }
  .social-square { width: 30px; height: 30px; background: #3b5a9a; }
  .header-social { left: 1018px; top: 158px; }

  /* Hero */
  .hero { left: 146px; top: 206px; width: 905px; height: 447px; display: flex; }
  .hero-photo {
    width: 363px; height: 100%;
    background: linear-gradient(160deg, #f4f1ec 0%, #e9e4dc 45%, #b08a66 78%, #6b4a33 100%);
  }
  .hero-panel { flex: 1; background: var(--accent-red); color: var(--white); position: relative; }
  .hero-kicker { position: absolute; left: 42px; top: 286px; font-size: 46px; font-weight: 300; line-height: 1; }
  .hero-title { position: absolute; left: 42px; top: 360px; font-size: 44px; font-weight: 300; line-height: 1; letter-spacing: 1px; }
  .slider-dots { left: 963px; top: 665px; display: flex; gap: 15px; }
  .slider-dots span { width: 19px; height: 19px; border-radius: 50%; background: #d5d5d5; }
  .slider-dots span.active { background: var(--accent-red); }

  /* Section headings */
  .section-head { left: 146px; width: 905px; height: 48px; }
  .section-mark { position: absolute; left: 6px; top: 2px; width: 40px; height: 40px; border-radius: 50%; background: #8a8a8a; }
  .section-title { position: absolute; left: 87px; top: 0; font-size: 24px; font-weight: 400; text-transform: uppercase; line-height: 1.3; }
  .section-rule { position: absolute; left: 87px; right: 0; top: 36px; height: 4px; background: var(--rule); }
  .section-underline { position: absolute; left: 87px; top: 35px; width: 100px; height: 6px; }
  .projects-head { top: 700px; }
  .projects-head .section-underline { background: var(--accent-green); }
  .profile-head { top: 1850px; }
  .profile-head .section-underline { background: var(--accent-teal); }

  /* Project grid */
  .project-card { width: 252px; }
  .project-photo { width: 252px; height: 377px; }
  .project-name { margin-top: 12px; font-size: 25px; color: var(--accent-green); line-height: 1.2; }
  .project-text { margin-top: 6px; font-size: 15.5px; line-height: 24px; color: var(--ink); }
  .more { color: var(--accent-red); font-weight: 600; }
  .col-1 { left: 146px; } .col-2 { left: 470px; } .col-3 { left: 797px; }
  .row-1 { top: 768px; } .row-2 { top: 1320px; }

  /* Profile */
  .profile-body { left: 146px; top: 1918px; width: 905px; }
  .profile-title { font-size: 27px; font-weight: 400; margin-bottom: 8px; }
  .profile-body p { font-size: 18.5px; line-height: 29px; margin-bottom: 24px; }
  .owner-photo {
    left: 146px; top: 2215px; width: 168px; height: 168px; background: var(--swatch);
    display: flex; align-items: center; justify-content: center;
    font-style: italic; font-size: 17px; color: #3a1a1a;
  }
  .owner-quote { left: 350px; top: 2248px; font-size: 19px; line-height: 31px; font-style: italic; }
  .owner-name { left: 355px; top: 2320px; font-size: 19px; }
  .owner-name strong { font-weight: 600; }

  /* Footer */
  .site-footer { left: 0; top: 2520px; width: 1200px; height: 360px; background: var(--footer-bg); color: var(--footer-text); }
  .footer-col { position: absolute; top: 42px; }
  .footer-col h3 { font-size: 19px; font-weight: 400; margin-bottom: 20px; }
  .footer-col ul { list-style: none; }
  .footer-col li { font-size: 15px; line-height: 29px; }
  .nav-col { left: 146px; } .legal-col { left: 305px; } .address-col { left: 456px; }
  .address-row { position: relative; padding-left: 46px; font-size: 14.5px; line-height: 29px; }
  .address-row svg { position: absolute; left: 2px; top: 6px; }
  .address-row + .address-row { margin-top: 6px; }
  .stay-connected { position: absolute; right: 149px; top: 42px; font-size: 14px; }
  .footer-social { position: absolute; left: 1020px; top: 72px; background: var(--white); }
  .copyright { position: absolute; right: 149px; top: 215px; font-size: 14px; }
</style>
</head>
<body>

<header>
  <div class="abs brand"><span>Wren Hollow</span><span class="brand-dot"></span></div>
  <nav class="abs main-nav">
    <ul>
      <li class="home">Home</li>
      <li class="projects">Projects</li>
      <li class="profile">Profile</li>
      <li class="contact">Contact</li>
    </ul>
  </nav>
  <div class="abs nav-rule"></div>
  <div class="abs nav-active"></div>
  <div class="abs social-square header-social" role="img" aria-label="Social page link"></div>
</header>

<section class="abs hero">
  <div class="hero-photo" role="img" aria-label="Photo of a bright living room with abstract painting and timber floor"></div>
  <div class="hero-panel">
    <div class="hero-kicker">featured project</div>
    <div class="hero-title">ALDER HOME</div>
  </div>
</section>
<div class="abs slider-dots"><span class="active"></span><span></span><span></span></div>

<div class="abs section-head projects-head">
  <span class="section-mark"></span>
  <h2 class="section-title">Projects</h2>
  <span class="section-rule"></span><span class="section-underline"></span>
</div>

<article class="abs project-card col-1 row-1">
  <div class="project-photo" role="img" aria-label="Photo of a lounge chair beside a kitchen bench" style="background:linear-gradient(170deg,#f3f1ee 0%,#e5ddd2 55%,#8c6a3e 85%,#5a4330 100%)"></div>
  <h3 class="project-name">Lorem Ipsum</h3>
  <p class="project-text">This is the project number one tra, erat sed fermentum feugiat, velit mauris egestas quam ......... <span class="more">&#8250;&#8250;</span></p>
</article>
<article class="abs project-card col-2 row-1">
  <div class="project-photo" role="img" aria-label="Photo of an armchair by a glass door" style="background:linear-gradient(170deg,#ecebe8 0%,#cfcac2 50%,#8e8478 80%,#4a3a2e 100%)"></div>
  <h3 class="project-name">Lorem Ipsum</h3>
  <p class="project-text">This is the project number one tra, erat sed fermentum feugiat, velit mauris egestas quam ......... <span class="more">&#8250;&#8250;</span></p>
</article>
<article class="abs project-card col-3 row-1">
  <div class="project-photo" role="img" aria-label="Photo of a teal chest of drawers under artwork" style="background:linear-gradient(170deg,#f4f3f1 0%,#e6e3de 45%,#2f9c9a 70%,#c9c2b4 100%)"></div>
  <h3 class="project-name">Lorem Ipsum</h3>
  <p class="project-text">This is the project number one tra, erat sed fermentum feugiat, velit mauris egestas quam ......... <span class="more">&#8250;&#8250;</span></p>
</article>
<article class="abs project-card col-1 row-2">
  <div class="project-photo" role="img" aria-label="Photo of a bedroom with pendant light" style="background:linear-gradient(170deg,#ecebea 0%,#d9d6d2 50%,#a9a39c 80%,#6e655d 100%)"></div>
  <h3 class="project-name">Lorem Ipsum</h3>
  <p class="project-text">This is the project number one tra, erat sed fermentum feugiat, velit mauris egestas quam ......... <span class="more">&#8250;&#8250;</span></p>
</article>
<article class="abs project-card col-2 row-2">
  <div class="project-photo" role="img" aria-label="Photo of a dining table with wall clock" style="background:linear-gradient(170deg,#eeecea 0%,#dcd6cf 45%,#8a6548 75%,#4d3526 100%)"></div>
  <h3 class="project-name">Lorem Ipsum</h3>
  <p class="project-text">This is the project number one tra, erat sed fermentum feugiat, velit mauris egestas quam ......... <span class="more">&#8250;&#8250;</span></p>
</article>
<article class="abs project-card col-3 row-2">
  <div class="project-photo" role="img" aria-label="Photo of a sitting room with red lamp" style="background:linear-gradient(170deg,#f2f1ef 0%,#ddd8d1 45%,#9d7b5c 78%,#5b412f 100%)"></div>
  <h3 class="project-name">Lorem Ipsum</h3>
  <p class="project-text">This is the project number one tra, erat sed fermentum feugiat, velit mauris egestas quam ......... <span class="more">&#8250;&#8250;</span></p>
</article>

<div class="abs section-head profile-head">
  <span class="section-mark"></span>
  <h2 class="section-title">Profile</h2>
  <span class="section-rule"></span><span class="section-underline"></span>
</div>

<section class="abs profile-body">
  <h3 class="profile-title">What is Wren Hollow ?</h3>
  <p>Wren Hollow is a design service and homewares store run by interior decorator Marion Tulk.</p>
  <p>Inspiration is drawn from passion for quality products... the homewares range is stylish and consists of unique furniture pieces, decor accessories and lighting, there is an evolving product range...</p>
  <p>Marion's qualification and work experience as an interior decorator means that she is able to provide advice and recommendations for interior and exterior concepts, colour consultations, furniture, lighting, decor concepts and products are sourced for individual projects. A re-upholstery service is also provided.</p>
</section>

<div class="abs owner-photo" role="img" aria-label="Portrait placeholder">Marion's Photo</div>
<blockquote class="abs owner-quote">“ We Provide the best for our<br>&nbsp;&nbsp;Customers....”</blockquote>
<p class="abs owner-name"><strong>Marion Tulk</strong> - Owner</p>

<footer class="abs site-footer">
  <div class="footer-col nav-col">
    <h3>Navigation</h3>
    <ul><li>Home</li><li>Project</li><li>Profile</li><li>Contact</li></ul>
  </div>
  <div class="footer-col legal-col">
    <h3>Legal</h3>
    <ul><li>Terms of use</li><li>Privacy Policy</li><li>Sitemap</li></ul>
  </div>
  <div class="footer-col address-col">
    <h3>Address</h3>
    <div class="address-row">
      <svg width="16" height="22" viewBox="0 0 16 22"><path d="M8 0C3.6 0 0 3.5 0 7.9 0 13.8 8 22 8 22s8-8.2 8-14.1C16 3.5 12.4 0 8 0z" fill="#fff"/><circle cx="8" cy="8" r="3" fill="#2a2927"/></svg>
      4/27 Tallow Lane, Marram Street,<br>Brinley West 3290<br>Victoria, Australia.
    </div>
    <div class="address-row">
      <svg width="20" height="14" viewBox="0 0 20 14"><rect width="20" height="14" fill="#fff"/><path d="M0 0l10 8 10-8" fill="none" stroke="#2a2927" stroke-width="1.6"/></svg>
      info@wrenhollow.com.au
    </div>
    <div class="address-row">
      <svg width="18" height="18" viewBox="0 0 18 18"><path d="M4 0l3 4-2 2.5c1 2.4 3 4.4 6.5 6.5L14 11l4 3-2.5 3.5C8 17 1 10 0.5 2.5z" fill="#fff"/></svg>
      03 5550 1290
    </div>
  </div>
  <div class="stay-connected">Stay Connected</div>
  <div class="social-square footer-social" role="img" aria-label="Social page link"></div>
  <div class="copyright">Copyright 2014 Wren Hollow. Al Rights Reserved</div>
</footer>

</body>
</html>
```